NFVPS Business Card Revamp: Professional and Modern Design for Enhanced Networking

The Northfield Veterinary Practitioner Society (NFVPS) is seeking a redesign of its current business cards to better represent its professional image and improve its networking capabilities. The NFVPS is a professional association for veterinary technologists in Alberta, Canada, and it aims to promote the welfare of animals and the veterinary profession through continuing education, advocacy, and professional development.

The project objectives are to create a professional and modern design for the NFVPS business cards that accurately reflects the organization's values and mission. We would like to include our brand colors in the final design and make it editable to update different roles and positions for the association. The card will need to include the name, pronouns (if applicable), and position of the individual as well as an email address, phone, and website.

The final deliverables for this project will include a design concept for the new NFVPS business cards, a layout for the business cards that includes all relevant contact information and branding elements, and final design files in an editable format.

Target Market(s)

Members, industry stakeholders, government

Industry/Entity Type

Veterinary

Contact Information for Business Card

Name, pronouns (if applicable), title, logo, website, email, phone number

Font styles to use
Other font styles liked:
• Open Sans, logo font is Politica

Requirements
Must have
• Brand recognition, logo, professional and modern design
Nice to have
• double-sided - open to single sided
Should not have
• pictures of animals, hearts

```html
<!DOCTYPE html>
<html lang="en">
<head>
<meta charset="utf-8">
<title>NFVPS Business Card</title>
<link rel="stylesheet" href="https://fonts.googleapis.com/css2?family=Open+Sans:wght@400;600;700&display=swap">
<style>
  :root {
    --backdrop: #8c8c8c;
    --card-teal: #5e7874;
    --card-white: #ffffff;
    --accent-green: #87ae56;
    --accent-blue: #63b6d1;
    --text-light: #ffffff;
    --card-radius: 34px;
  }
  * { box-sizing: border-box; margin: 0; padding: 0; }
  html, body {
    width: 1200px;
    height: 1122px;
    overflow: hidden;
    background: var(--backdrop);
    font-family: "Open Sans", sans-serif;
  }
  .sheet {
    position: relative;
    width: 1200px;
    height: 1122px;
  }
  .card {
    position: absolute;
    top: 206px;
    width: 420px;
    height: 710px;
    border-radius: var(--card-radius);
    overflow: hidden;
    background: var(--card-teal);
    box-shadow: 0 8px 18px rgba(0,0,0,0.35);
  }
  .card--front { left: 150px; }
  .card--back { left: 630px; }

  /* Front */
  .front-divide {
    position: absolute;
    inset: 0 0 auto 0;
    width: 420px;
    height: 380px;
  }
  .front-brand {
    position: absolute;
    top: 120px;
    left: 44px;
    display: flex;
    align-items: center;
    gap: 12px;
    color: var(--card-teal);
    font-weight: 700;
    font-size: 46px;
    line-height: 1;
    letter-spacing: 2px;
  }
  .brand-dot {
    width: 26px;
    height: 26px;
    border-radius: 50%;
    background: var(--accent-green);
    flex: none;
  }
  .holder {
    position: absolute;
    top: 420px;
    left: 0;
    width: 100%;
    text-align: center;
    color: var(--text-light);
  }
  .holder-name {
    font-weight: 700;
    font-size: 29px;
    letter-spacing: 1px;
    text-transform: uppercase;
  }
  .holder-role {
    display: flex;
    align-items: center;
    justify-content: center;
    gap: 10px;
    margin-top: 4px;
    font-size: 20px;
    font-weight: 400;
    letter-spacing: 1px;
  }
  .holder-role::before,
  .holder-role::after {
    content: "";
    width: 62px;
    height: 1px;
    background: var(--text-light);
  }
  .contact-icons {
    display: flex;
    justify-content: center;
    gap: 8px;
    margin-top: 22px;
  }
  .contact-icons svg { width: 28px; height: 28px; }
  .contact-lines {
    margin-top: 16px;
    list-style: none;
    font-size: 21px;
    line-height: 1.45;
    letter-spacing: 0.5px;
  }

  /* Back */
  .back-brand {
    position: absolute;
    top: 0;
    left: 0;
    width: 100%;
    height: 100%;
    display: flex;
    flex-direction: column;
    align-items: center;
    justify-content: center;
    color: var(--text-light);
    font-weight: 400;
  }
  .back-mark {
    display: flex;
    align-items: center;
    gap: 14px;
    font-size: 78px;
    letter-spacing: 3px;
    line-height: 1;
  }
  .back-mark .brand-dot { width: 30px; height: 30px; }
  .back-name {
    margin-top: 14px;
    font-size: 15px;
    letter-spacing: 0.5px;
  }
</style>
</head>
<body>
<main class="sheet">
  <section class="card card--front">
    <svg class="front-divide" viewBox="0 0 420 380" aria-hidden="true">
      <path d="M0 0 H420 V70 C330 150 250 250 200 380 H0 Z" fill="var(--card-white)"/>
    </svg>
    <div class="front-brand"><span class="brand-dot"></span>NFVPS</div>
    <div class="holder">
      <h1 class="holder-name">Dana Whitfield, RVT</h1>
      <p class="holder-role">President</p>
      <div class="contact-icons">
        <svg viewBox="0 0 28 28" aria-label="phone" role="img">
          <circle cx="14" cy="14" r="14" fill="var(--text-light)"/>
          <path d="M9.5 8 L12 8 L13 11 L11.5 12.3 Q13 15.2 15.7 16.5 L17 15 L20 16 L20 18.5 Q19.5 20 18 20 Q12 19.5 8 12 Q8 8.5 9.5 8 Z" fill="var(--card-teal)"/>
        </svg>
        <svg viewBox="0 0 28 28" aria-label="email" role="img">
          <circle cx="14" cy="14" r="14" fill="var(--text-light)"/>
          <rect x="7.5" y="9.5" width="13" height="9" fill="none" stroke="var(--card-teal)" stroke-width="1.5"/>
          <path d="M7.5 9.5 L14 15 L20.5 9.5" fill="none" stroke="var(--card-teal)" stroke-width="1.5"/>
        </svg>
        <svg viewBox="0 0 28 28" aria-label="website" role="img">
          <circle cx="14" cy="14" r="14" fill="var(--text-light)"/>
          <circle cx="14" cy="14" r="6.5" fill="none" stroke="var(--card-teal)" stroke-width="1.5"/>
          <ellipse cx="14" cy="14" rx="2.8" ry="6.5" fill="none" stroke="var(--card-teal)" stroke-width="1.3"/>
          <path d="M7.5 14 H20.5" stroke="var(--card-teal)" stroke-width="1.3"/>
        </svg>
      </div>
      <ul class="contact-lines">
        <li>555-014-2278</li>
        <li>info@nfvps.org</li>
        <li>www.nfvps.org</li>
      </ul>
    </div>
  </section>

  <section class="card card--back">
    <div class="back-brand">
      <div class="back-mark"><span class="brand-dot"></span>NFVPS</div>
      <p class="back-name">Northfield Veterinary Practitioner Society</p>
    </div>
  </section>
</main>
</body>
</html>
```